High end cable company busines card and letterhead

Dear designers,
We assemble high end audio cables that cost a couple of hundred dollars per piece and we are improving the looks of the product.
When people buy a cable they get a leather pouch with the invoice (letterhead) , a business card of the maker and also a quality control card  / warranty card.
The quality control card  is the same size as a business card and the back of the quality control card is the same back as the business card. So we need 4 things:
-1 back of a business card
-1 front of a business card (a file where we can change the name and details of the worker)
-1 quality control front (I will add a photo of an example)
-1 letterhead
We want to make letterpress business cards and use shiny foil for the logo’s. We like the colors black and copper or black and gold for the back. The front of the business card can also be black, copper and white but it does not have to be those colors. We want people to have the feeling that they bought something expensive and high quality.
The front of the quality control card has to be white so we can check things off with a sharpie / pen.
What has to be on the cards:
Business card:
- Our Logo
-Text: Meet the maker (people get the business card of the one who made the cable)
-Name
-Address
-Website (www.tallowfenwire.com)
-Email address
-Text: For any advise or questions about your cable feel free to contact me.
What has to be on the quality control card:
-Our logo
-Text: quality controll and warranty card (small at the bottom)
-text:
Assembled by:________________
Date: ______-______-____________
QC by:_________________________

Assembly QC [   ]
Measurement QC [   ]
Aesthetics [   ]
(The box [    ] is for the initials of the person that does the QC, it can also be a line or something else)
The letterhead can be your own idea as long as it looks luxurious.
You can download our logo. We have a black one and gold / black but you can change the Color to Match your design. (For instance copper or something) There is also a white one that can be used with the icon on the left.
Some links of stuff we like:
-https://clipvault.example/Kq3rLm8zXa1 (The looks of this card maybe a bit less busy looking)
-https://b.brindlemart.example/_pRxwQaf
-https://b.brindlemart.example/_pTj4Wob
-https://b.brindlemart.example/_pYeuZ11

```html
<!DOCTYPE html>
<html lang="en">
<head>
<meta charset="utf-8">
<title>Tallow Fen — Stationery</title>
<link href="https://fonts.googleapis.com/css2?family=EB+Garamond:ital,wght@0,400;0,500;1,400&family=Playfair+Display:ital,wght@0,400;0,700;0,900;1,700&family=PT+Sans&display=swap" rel="stylesheet">
<style>
  :root{
    --board:#9b9b9b;
    --ink:#0b0c0e;
    --ink-soft:#17191d;
    --gold:#f2c20f;
    --gold-deep:#c99a06;
    --gold-haze:rgba(201,154,6,.16);
    --paper:#ffffff;
    --label:#111111;
    --form-ink:#222222;
    --body-text:#e6e6e6;
  }
  *{margin:0;padding:0;box-sizing:border-box}
  html,body{width:1200px;height:849px;overflow:hidden}
  body{background:var(--board);position:relative;font-family:"EB Garamond",serif}

  .section-label{position:absolute;font-family:"PT Sans",sans-serif;font-size:23px;color:var(--label);transform:translateX(-50%);white-space:nowrap;line-height:1}

  .card{position:absolute;left:130px;width:254px;height:145px;background:var(--ink);overflow:hidden;box-shadow:3px 5px 8px rgba(0,0,0,.35)}
  .foil-field{position:absolute;left:0;top:0;width:130px;height:145px;background:linear-gradient(125deg,var(--ink-soft) 0%,var(--gold-haze) 45%,var(--ink) 100%)}

  .wordmark{position:absolute;font-family:"EB Garamond",serif;font-weight:500;color:var(--gold);letter-spacing:.28em;white-space:nowrap;text-align:center;transform:translateX(-50%);line-height:1}
  .wordmark .dot{display:inline-block;width:.55em;height:.55em;background:var(--gold);margin-right:.4em;vertical-align:.12em}

  .card-front .name{position:absolute;left:131px;top:89px;font-family:"Playfair Display",serif;font-weight:700;font-style:italic;font-size:9.5px;color:var(--gold)}
  .card-front .contact{position:absolute;left:131px;font-family:"EB Garamond",serif;font-size:7px;color:var(--gold-deep)}

  .maker-title{position:absolute;left:0;right:0;top:51px;text-align:center;font-family:"Playfair Display",serif;font-weight:900;font-size:7.6px;letter-spacing:.08em;color:var(--gold)}
  .maker-note{position:absolute;left:0;right:0;top:67px;text-align:center;font-family:"EB Garamond",serif;font-size:7.2px;line-height:9px;color:var(--gold)}

  .warranty .foil-field{width:113px}
  .form-panel{position:absolute;left:0;top:0;width:254px;height:145px}
  .form{position:absolute;font-family:"EB Garamond",serif;font-size:6.2px;color:var(--form-ink);white-space:nowrap}
  .form .rule{display:inline-block;border-bottom:.6px solid var(--form-ink);height:6px;vertical-align:-1px}
  .initials{position:absolute;left:193px;width:41px;height:5px;border:.6px solid var(--form-ink);border-top:none}
  .warranty-title{position:absolute;left:124px;width:130px;top:119px;text-align:center;font-family:"Playfair Display",serif;font-weight:700;font-size:6px;letter-spacing:.05em;color:var(--form-ink)}

  .letterhead{position:absolute;left:532px;top:112px;width:501px;height:649px;background:linear-gradient(160deg,#121417,#08090b 55%,#0d0e10);overflow:hidden;box-shadow:4px 6px 12px rgba(0,0,0,.35)}
  .letterhead .foil-field{width:501px;height:290px;background:linear-gradient(160deg,var(--gold-haze) 0%,var(--ink-soft) 40%,rgba(8,9,11,0) 100%)}
  .lh-heading{position:absolute;left:0;right:0;top:228px;text-align:center;font-family:"Playfair Display",serif;font-weight:900;font-size:24px;letter-spacing:.05em;color:var(--gold)}
  .lh-body{position:absolute;left:118px;width:302px;font-family:"EB Garamond",serif;font-size:8.1px;line-height:11.5px;color:var(--body-text)}
  .lh-body p{margin-bottom:11.5px}
  .lh-body p.tight{margin-bottom:0}
  .lh-sub{position:absolute;left:100px;width:338px;top:440px;text-align:center;font-family:"Playfair Display",serif;font-size:14.4px;line-height:19px;letter-spacing:.07em;color:var(--gold)}
  .lh-web{position:absolute;right:87px;top:616px;font-family:"Playfair Display",serif;font-weight:700;font-size:9.5px;letter-spacing:.12em;color:var(--gold)}
</style>
</head>
<body>

<div class="section-label" style="left:256px;top:37px">Business card</div>
<div class="section-label" style="left:256px;top:436px">Warranty card</div>
<div class="section-label" style="left:779px;top:37px">Letterhead</div>

<!-- Business card front -->
<div class="card card-front" style="top:85px">
  <div class="foil-field" role="img" aria-label="Gold foil diagonal line decoration"></div>
  <div class="wordmark" style="left:163px;top:53px;font-size:11px"><span class="dot"></span>TALLOW FEN</div>
  <div class="name">Name Surname</div>
  <div class="contact" style="top:103px">name@tallowfenwire.com</div>
  <div class="contact" style="top:116px">www.tallowfenwire.com</div>
</div>

<!-- Business card back -->
<div class="card card-back" style="top:249px">
  <div class="foil-field" role="img" aria-label="Gold foil diagonal line decoration"></div>
  <div class="maker-title">MEET THE MAKER</div>
  <div class="maker-note">For any advise or questions about your cable<br>feel free to contact me.</div>
</div>

<!-- Warranty card front -->
<div class="card warranty" style="top:481px">
  <div class="foil-field" role="img" aria-label="Gold foil diagonal line decoration"></div>
  <svg class="form-panel" viewBox="0 0 254 145" aria-hidden="true">
    <polygon points="113,0 254,0 254,145 113,145 113,102 124,80 113,62" fill="var(--paper)"/>
  </svg>
  <div class="wordmark" style="left:62px;top:66px;font-size:9px"><span class="dot"></span>TALLOW FEN</div>
  <div class="form" style="left:135px;top:23px">Assembled by: <span class="rule" style="width:53px"></span></div>
  <div class="form" style="left:135px;top:37px">Date: <span class="rule" style="width:18px"></span>-<span class="rule" style="width:18px"></span>-<span class="rule" style="width:38px"></span></div>
  <div class="form" style="left:135px;top:51px">QC by: <span class="rule" style="width:77px"></span></div>
  <div class="form" style="left:135px;top:76px">Assembly QC</div>
  <div class="initials" style="top:79px"></div>
  <div class="form" style="left:135px;top:86px">Measurement QC</div>
  <div class="initials" style="top:89px"></div>
  <div class="form" style="left:135px;top:96px">Aesthetics</div>
  <div class="initials" style="top:99px"></div>
  <div class="warranty-title">quality controll and warranty card</div>
</div>

<!-- Warranty card back -->
<div class="card card-back" style="top:645px">
  <div class="foil-field" role="img" aria-label="Gold foil diagonal line decoration"></div>
  <div class="maker-title">MEET THE MAKER</div>
  <div class="maker-note">For any advise or questions about your cable<br>feel free to contact me.</div>
</div>

<!-- Letterhead -->
<div class="letterhead">
  <div class="foil-field" role="img" aria-label="Gold foil diagonal stripe and chevron decoration across the top"></div>
  <div class="wordmark" style="left:269px;top:165px;font-size:26px"><span class="dot"></span>TALLOW FEN</div>

  <div class="lh-heading">Ipsum nesequa eperibus</div>

  <div class="lh-body" style="top:266px">
    <p>Idit, occumquas corestorio beriassi repudaes aliciist, ommolore quas ex et faces sed ut etument harcili cidiam restioribus assed quo voluptati a dolumqui doloribus, sit evelest ionsedis molupta tincil molupta di quiam et quos exceatemos aut harum si inctiur, sunt eium, sim dollorpore, viduciasi dolo maximoluptas consequi dolum quunt rest, quunt.</p>
    <p>Beatur moloreiuntin commolorro officia si ut pliqui simagnam fugitio nseditaquiae nulparum quis exces esse plignih iligendamus ma illo quia simodi ant accumqu aeptas et officiis esciis in est venda ipsandit, natiur molorum imaiorunt.</p>
    <p>Culpa ne sit quam cuptiundi blaborate nis ent molupta tiberum ut aliquiant volest, secti doluptaqui nos accuptatur abor sus, sectaep tibus, con pererita cusandant laborati blabo. Et volorem velia eumqui acesed mollabo. Ut verepudam volor as dolorum qui ut asincturibus etur? Soluptatate ipsam alit, temo dolesequias alit, officiae con consectias dis nemque poreres aligent.</p>
  </div>

  <div class="lh-sub">Ipsum nesequa eperibus, voles plabor<br>aut et aut ut ut vitatis</div>

  <div class="lh-body" style="top:486px">
    <p class="tight">Quid mo vitate exero esciate plicaborest labor sit, inctin es core commolore volla doluptatio od est aut fugia dolorit invelique nobis volorehenit quibust dolume sit re nullatetur, aditis doluptia cuptate lit que conserionsed ent apel inveriorro consequibere nisque volorepro et quat.</p>
    <p class="tight">Officim aximuscium facculles reium fuga. Nequid quis experspis quid quas aute everspe reicium conse doluptam lacea corent, senectem et, nonsequi sed endae consect enissume vent as eationseque el ipsanis et odipsandae vit doluptatur sedis es aut fugit veliberum harchic to to estios plit, nobitat iasperum ut a cone nonsectae laboria volentionem qui con num etus poritiis aut omnim accumet ommodig enduciminime aut acea et incias velestiasit, utas rerchil ligendus is eum fugia sincide plam et que volut alictem</p>
  </div>

  <div class="lh-web">www.tallowfenwire.com</div>
</div>

</body>
</html>
```